TELVORIQ HOA Portal Site for Public

Clean up and organize current website; need website to look good and functional; this is a HOA (homeowner association management) website where homeowners can login and pay their bill, general information about a HOA, monthly newsletter page.
Competitors:
https://plumbrivet.com/
https://duskorrahill.com/
https://www.qxlivingspan.com/nevada
http://www.bpt-hoa.com/

Target Market(s)

homeowners

Industry/Entity Type

Real Estate

Coding

Coded - Design and coding required

Number of Pages Required

5+ page

Font styles to use
Serif

Colors
0292cd
33a6d7
e667a6
e34297

Requirements
Must have
• login to pay
• services page
• contact us
• order resale package
Nice to have
• page why an HOA would contract us

```html
<!DOCTYPE html>
<html lang="en">
<head>
<meta charset="utf-8">
<title>Telvoriq – Contact us</title>
<link href="https://fonts.googleapis.com/css2?family=Noto+Sans:wght@400;600&family=Tinos:wght@700&display=swap" rel="stylesheet">
<style>
  :root {
    --topbar: #007bff;
    --header: #ffc107;
    --ink: #212529;
    --nav: #6b5a14;
    --hero-title: #a6dbe8;
    --white: #ffffff;
    --rule: #dcdcdc;
    --accent-line: #e34297;
  }
  * { box-sizing: border-box; margin: 0; padding: 0; }
  html, body { width: 1042px; height: 1200px; overflow: hidden; background: var(--white); }
  body { font-family: "Noto Sans", Arial, sans-serif; color: var(--ink); position: relative; }

  .topbar { height: 75px; background: var(--topbar); position: relative; }
  .topbar-contact { position: absolute; left: 15px; top: 17px; font-family: "Tinos", "Times New Roman", serif; font-weight: 700; font-size: 14px; display: flex; align-items: center; gap: 4px; color: var(--ink); }
  .topbar-contact svg { display: block; }
  .topbar-tagline { position: absolute; left: 622px; top: 17px; font-size: 14px; }
  .login-button { position: absolute; right: 14px; top: 15px; font-size: 14px; padding: 5px 10px 6px; border-right: 2px solid var(--accent-line); border-bottom: 2px solid var(--accent-line); color: var(--ink); text-decoration: none; }

  .site-header { height: 106px; background: var(--header); position: relative; }
  .brand-name { position: absolute; left: 16px; top: 14px; font-size: 35px; font-weight: 400; line-height: 1.2; }
  .brand-tagline { position: absolute; left: 16px; top: 141px; top: 66px; font-size: 18px; }
  .main-nav { position: absolute; right: 20px; top: 44px; display: flex; gap: 15px; font-size: 14.5px; }
  .main-nav a { color: var(--nav); text-decoration: none; }
  .main-nav a.is-current { color: var(--ink); }

  .hero { height: 588px; position: relative; }
  .hero-photo { position: absolute; inset: 0; background: linear-gradient(100deg, #b86f5a 0%, #6a5a46 22%, #2f7a6c 34%, #8a6a4a 48%, #d9c98c 62%, #c85a8a 78%, #9a6a4a 100%); }
  .hero-title { position: absolute; left: 155px; top: 493px; top: 292px; font-size: 37px; font-weight: 600; color: var(--hero-title); }
  .hero-subtitle { position: absolute; left: 157px; top: 366px; font-size: 18px; color: var(--white); }

  .contact { padding: 6px 14px 0; position: relative; height: 352px; }
  .contact-title { font-size: 36px; font-weight: 600; line-height: 1.1; }
  .offices { display: grid; grid-template-columns: 535px 1fr; margin-top: 8px; }
  .office h3 { font-size: 25px; font-weight: 400; line-height: 1.2; margin-bottom: 6px; }
  .office p { font-size: 14px; line-height: 1.3; margin-bottom: 19px; }

  .site-footer { position: absolute; left: 10px; right: 0; top: 1120px; border-top: 1px solid var(--rule); height: 80px; }
  .copyright { position: absolute; left: 26px; top: 26px; font-size: 14px; }
  .social { position: absolute; left: 795px; top: 28px; display: flex; gap: 20px; align-items: center; }
  .social span { width: 11px; height: 11px; background: var(--ink); display: block; }
</style>
</head>
<body>
  <div class="topbar">
    <div class="topbar-contact">
      <svg width="13" height="13" viewBox="0 0 13 13"><circle cx="6.5" cy="6.5" r="5.5" fill="none" stroke="#212529" stroke-width="1.6"/><circle cx="6.5" cy="6.5" r="2" fill="#212529"/></svg>
      <span>000 123 456 789</span>
      <svg width="14" height="11" viewBox="0 0 14 11"><rect x="0" y="0" width="14" height="11" rx="1" fill="#212529"/><path d="M1 1.5 L7 6 L13 1.5" stroke="#007bff" stroke-width="1.2" fill="none"/></svg>
      <span>NAME@EMAIL.COM</span>
    </div>
    <div class="topbar-tagline">Lets work together</div>
    <a class="login-button" href="#">Homeowner log-in</a>
  </div>

  <header class="site-header">
    <h1 class="brand-name">Telvoriq</h1>
    <div class="brand-tagline">Homeowner association management</div>
    <nav class="main-nav">
      <a href="#">Homeowner</a>
      <a href="#">Services</a>
      <a href="#" class="is-current">Contact us</a>
      <a href="#">order resale package</a>
    </nav>
  </header>

  <section class="hero">
    <div class="hero-photo" role="img" aria-label="Photo of a small child playing with a toy house in a colourful playroom"></div>
    <h2 class="hero-title">If you had any problems contact us</h2>
    <p class="hero-subtitle">We are here to help</p>
  </section>

  <section class="contact">
    <h2 class="contact-title">contact</h2>
    <div class="offices">
      <div class="office">
        <h3>Our office</h3>
        <p>61837 Dunmore Road Near Oak Plaza, U.S</p>
        <p>Phone: 012-12345678</p>
        <p>Email: info@telvoriq.org</p>
      </div>
      <div class="office">
        <h3>city office</h3>
        <p>61837 Dunmore Road Near Oak Plaza, U.S</p>
        <p>Phone: 012-12345678</p>
        <p>Email: info@telvoriq.org</p>
      </div>
      <div class="office">
        <h3>Mailing address</h3>
        <p>61837 Dunmore Road Near Oak Plaza, U.S</p>
        <p>Phone: 012-12345678</p>
        <p>Email: info@telvoriq.org</p>
      </div>
      <div class="office">
        <h3>Our office</h3>
        <p>61837 Dunmore Road Near Oak Plaza, U.S</p>
        <p>Phone: 012-12345678</p>
        <p>Email: info@telvoriq.org</p>
      </div>
    </div>
  </section>

  <footer class="site-footer">
    <p class="copyright">COPYRIGHT 2019 TELVORIQ. | ALL RIGHTS RESERVED</p>
    <div class="social">
      <span aria-label="Social link"></span>
      <span aria-label="Social link"></span>
      <svg width="14" height="14" viewBox="0 0 14 14" aria-label="Phone"><path d="M3 1 L5.5 1 L6.5 4 L5 5.5 C6 7.5 7 8.5 8.5 9 L10 7.5 L13 8.5 L13 11 C13 12 12 13 11 13 C6 12.5 1.5 8 1 3 C1 2 2 1 3 1 Z" fill="#212529"/></svg>
      <span aria-label="Social link"></span>
    </div>
  </footer>
</body>
</html>
```